CoveysArmsPersonal

I am a cutting edge, top of the line gun store. We are expanding faster than we can keep up. We offer: Gunsmithing, Transfers, Concealed Carry, Machine Guns, Suppressors. My colors are reflected in my logo. Red, black and white. I like a clean design that gets the point across. I was trying to find a plastic business card, but will settle with a high quality paper product.

Contact Information for Business Card

Dwayne Covey - Owner
620-514-8826 (Cell)
Covey's Range Outfitters
1847 E. Hwy 9
Vessin, KS 67462
sales@coveysrangeoutfitters.com
coveysrangeoutfitters.com

```html
<!DOCTYPE html>
<html lang="en">
<head>
<meta charset="utf-8">
<title>Covey's Range Outfitters – Business Card</title>
<link rel="stylesheet" href="https://fonts.googleapis.com/css2?family=Oswald:wght@500;600&family=Arimo:wght@400;700&display=swap">
<style>
  :root {
    --ink: #0b0c0c;
    --crimson: #8c0d08;
    --paper: #ffffff;
    --steel: #8d9594;
    --steel-light: #dfe3e2;
  }
  html, body {
    margin: 0;
    padding: 0;
    overflow: hidden;
    background: var(--paper);
  }
  .card {
    position: relative;
    width: 1200px;
    height: 720px;
    overflow: hidden;
    background: linear-gradient(90deg, var(--paper) 0%, var(--paper) 55%, var(--steel-light) 78%, var(--steel) 100%);
    font-family: "Arimo", Arial, sans-serif;
  }
  .impact-art {
    position: absolute;
    left: 906px;
    top: 116px;
    width: 184px;
    height: 226px;
    border-radius: 46% 54% 50% 50%;
    background: radial-gradient(ellipse at 45% 45%, #3e4242 0%, #6b7070 45%, #b9bebd 75%, rgba(220,224,223,0) 100%);
  }
  .brand {
    position: absolute;
    left: 0;
    width: 1174px;
    top: 44px;
    text-align: center;
  }
  .brand-mark {
    display: block;
    margin: 0 auto 44px;
    width: 120px;
    height: 120px;
    border-radius: 50%;
    background: var(--crimson);
  }
  .brand-name {
    font-family: "Oswald", sans-serif;
    font-weight: 600;
    font-size: 42px;
    letter-spacing: 3px;
    color: var(--ink);
    line-height: 1;
    text-transform: uppercase;
  }
  .identity {
    position: absolute;
    right: 802px;
    top: 306px;
    text-align: right;
  }
  .person-name {
    font-family: "Oswald", sans-serif;
    font-weight: 500;
    font-size: 40px;
    line-height: 1.1;
    color: var(--ink);
    text-transform: uppercase;
  }
  .person-role {
    font-family: "Oswald", sans-serif;
    font-weight: 500;
    font-size: 24px;
    color: var(--crimson);
    text-transform: uppercase;
    margin-top: 4px;
  }
  .address {
    font-size: 31px;
    font-weight: 700;
    color: var(--crimson);
    line-height: 1.05;
    margin-top: 24px;
  }
  .divider {
    position: absolute;
    left: 411px;
    top: 306px;
    width: 4px;
    height: 186px;
    background: var(--crimson);
  }
  .contact-list {
    position: absolute;
    left: 428px;
    top: 296px;
    margin: 0;
    padding: 0;
    list-style: none;
  }
  .contact-row {
    display: flex;
    align-items: baseline;
    height: 48px;
  }
  .contact-key {
    width: 50px;
    text-align: center;
    font-size: 36px;
    color: var(--crimson);
  }
  .contact-value {
    color: var(--ink);
    font-weight: 700;
    font-size: 26px;
    text-transform: uppercase;
  }
  .contact-value.phone {
    font-size: 37px;
  }
  .waves {
    position: absolute;
    left: 0;
    top: 0;
  }
</style>
</head>
<body>
<main class="card">
  <div class="impact-art" role="img" aria-label="Bullet hole torn through grey metal"></div>

  <svg class="waves" width="1200" height="720" viewBox="0 0 1200 720" aria-hidden="true">
    <path d="M0 512 C150 540 300 600 480 592 C700 578 850 516 1012 508 C850 526 700 600 480 624 C300 645 150 602 0 574 Z" fill="var(--crimson)"/>
    <path d="M0 586 C200 600 300 668 500 642 C700 616 850 520 1200 510 L1200 720 L0 720 Z" fill="var(--ink)"/>
  </svg>

  <header class="brand">
    <span class="brand-mark"></span>
    <div class="brand-name">Covey's Range Outfitters</div>
  </header>

  <section class="identity">
    <div class="person-name">Dwayne Covey</div>
    <div class="person-role">Owner</div>
    <div class="address">1847 E. Hwy 9<br>Vessin, KS 67462</div>
  </section>

  <div class="divider"></div>

  <ul class="contact-list">
    <li class="contact-row"><span class="contact-key">C</span><span class="contact-value phone">:(620)-514-8826</span></li>
    <li class="contact-row"><span class="contact-key">E</span><span class="contact-value">:sales@coveysrangeoutfitters.com</span></li>
    <li class="contact-row"><span class="contact-key">W</span><span class="contact-value">:coveysrangeoutfitters.com</span></li>
  </ul>
</main>
</body>
</html>
```